Business Card Design for a Residential Engineering Company

We need a business card designed for a residential engineering company.
We would like:
White background on the front of the card
Colors coordinating with the Logo
Double Sided
Clean design

Card Info Front:
Brindlecrest
Darnell Okafor, Owner
416-555-0193
darnell@brindlecrest.ca
www.brindlecrest.ca

Card Info Back:
Services
Building Permits
Engineering Stamping
Architectural Drawings
Engineer Certification Letter
Engineer Site Inspection and Report
Load Bearing Wall Removal
Structural Beam Designs
Structural Column/Post Designs
Foundation Designs
Foundation Underpinning
Basement Lowering
Structural QRW, LVL and Timber Designs
Structural Steel Designs
Masonry Concrete Designs
Basement Designs
Commercial Designs
Timber Deck Designs
Construction Project Management.

We have included an example of the type of design the customer liked for the back of the card to make it easier to display all of the services.
We require the final output in PDF, with AND without crop marks, we will also require all source files with layers intact for future editing

```html
<!DOCTYPE html>
<html lang="en">
<head>
<meta charset="utf-8">
<title>Brindlecrest Business Card</title>
<link href="https://fonts.googleapis.com/css2?family=Roboto:wght@400;500;700&display=swap" rel="stylesheet">
<style>
  :root {
    --bg: #3b3c3f;
    --orange: #f7941d;
    --blue: #29a8e0;
    --blue-dark: #1e8fc4;
    --white: #ffffff;
    --ink: #222426;
  }
  * { margin: 0; padding: 0; box-sizing: border-box; }
  html, body { width: 1200px; height: 900px; overflow: hidden; }
  body {
    background: var(--bg);
    font-family: "Roboto", Arial, sans-serif;
    position: relative;
  }
  .card {
    position: absolute;
    left: 290px;
    width: 620px;
    height: 354px;
    border-radius: 24px;
    overflow: hidden;
  }
  /* Back side */
  .card-back { top: 68px; background: var(--blue); }
  .back-band {
    position: absolute; left: 0; top: 0; width: 100%; height: 80px;
    background: var(--orange);
  }
  .back-brand {
    position: absolute; left: 40px; top: 42px;
    font-size: 30px; line-height: 36px; font-weight: 700; letter-spacing: 1px;
    text-transform: uppercase; color: var(--white);
  }
  .services-title {
    position: absolute; left: 40px; top: 98px;
    font-size: 17px; line-height: 20px; font-weight: 700; color: var(--white);
    padding-bottom: 3px; border-bottom: 2px solid var(--white);
  }
  .service-list {
    position: absolute; list-style: none;
    color: var(--white); font-size: 13.5px; line-height: 20px;
  }
  .service-list li::before { content: "\2022"; margin-right: 7px; }
  .service-list.left { left: 44px; top: 130px; }
  .service-list.right { left: 330px; top: 92px; }

  /* Front side */
  .card-front { top: 478px; background: var(--white); }
  .front-brand {
    position: absolute; left: 40px; top: 166px;
    display: flex; align-items: center; gap: 10px;
  }
  .front-brand .mark { width: 14px; height: 14px; background: var(--orange); }
  .front-brand .name {
    font-size: 32px; font-weight: 700; letter-spacing: 1px;
    text-transform: uppercase; color: var(--blue);
  }
  .divider {
    position: absolute; left: 372px; top: 70px;
    width: 2px; height: 186px; background: var(--blue);
  }
  .contact { position: absolute; left: 392px; top: 74px; }
  .person-name { font-size: 22px; font-weight: 700; color: var(--blue); }
  .person-role { font-size: 14px; color: var(--ink); margin-top: 2px; }
  .contact-list { list-style: none; margin-top: 18px; }
  .contact-list li {
    display: flex; align-items: center; gap: 12px;
    font-size: 14.5px; color: var(--ink); height: 30px;
  }
  .contact-list svg { width: 18px; height: 18px; flex: none; fill: var(--blue-dark); }
</style>
</head>
<body>

<section class="card card-back" aria-label="Card back">
  <div class="back-band"></div>
  <div class="back-brand">Brindlecrest</div>
  <h2 class="services-title">Services</h2>
  <ul class="service-list left">
    <li>Building Permits</li>
    <li>Architectural Drawings</li>
    <li>Engineer Site Inspection and Report</li>
    <li>Structural Beam Designs</li>
    <li>Foundation Designs</li>
    <li>Basement Lowering</li>
    <li>Structural Steel Designs</li>
    <li>Basement Designs</li>
    <li>Timber Deck Designs</li>
  </ul>
  <ul class="service-list right">
    <li>Engineering Stamping</li>
    <li>Engineer Certification Letter</li>
    <li>Load Bearing Wall Removal</li>
    <li>Structural Column/Post Designs</li>
    <li>Foundation Underpinning</li>
    <li>Structural QRW, LVL and Timber Designs</li>
    <li>Masonry Concrete Designs</li>
    <li>Commercial Designs</li>
    <li>Construction Project Management.</li>
  </ul>
</section>

<section class="card card-front" aria-label="Card front">
  <div class="front-brand">
    <span class="mark"></span>
    <span class="name">Brindlecrest</span>
  </div>
  <div class="divider"></div>
  <div class="contact">
    <div class="person-name">Darnell Okafor</div>
    <div class="person-role">Owner</div>
    <ul class="contact-list">
      <li>
        <svg viewBox="0 0 24 24" aria-hidden="true"><path d="M6.6 10.8a15.1 15.1 0 0 0 6.6 6.6l2.2-2.2c.3-.3.7-.4 1-.2 1.1.4 2.3.6 3.6.6.6 0 1 .4 1 1V20c0 .6-.4 1-1 1A17 17 0 0 1 3 4c0-.6.4-1 1-1h3.5c.6 0 1 .4 1 1 0 1.3.2 2.5.6 3.6.1.3 0 .7-.2 1z"/></svg>
        416-555-0193
      </li>
      <li>
        <svg viewBox="0 0 24 24" aria-hidden="true"><path d="M3 5h18c.6 0 1 .4 1 1v12c0 .6-.4 1-1 1H3c-.6 0-1-.4-1-1V6c0-.6.4-1 1-1zm9 7.2L20 7H4zm0 2.3L4 9.3V17h16V9.3z"/></svg>
        darnell@brindlecrest.ca
      </li>
      <li>
        <svg viewBox="0 0 24 24" aria-hidden="true"><path d="M12 2a10 10 0 1 0 0 20 10 10 0 0 0 0-20zm6.9 6h-3a15.7 15.7 0 0 0-1.4-3.6A8 8 0 0 1 18.9 8zM12 4c.8 1.2 1.5 2.5 1.9 4h-3.8c.4-1.5 1.1-2.8 1.9-4zM4.3 14a8 8 0 0 1 0-4h3.4a16.5 16.5 0 0 0 0 4zm.8 2h3a15.7 15.7 0 0 0 1.4 3.6A8 8 0 0 1 5.1 16zm3-8h-3a8 8 0 0 1 4.4-3.6A15.7 15.7 0 0 0 8.1 8zM12 20c-.8-1.2-1.5-2.5-1.9-4h3.8c-.4 1.5-1.1 2.8-1.9 4zm2.3-6H9.7a14.7 14.7 0 0 1 0-4h4.6a14.7 14.7 0 0 1 0 4zm.2 5.6c.6-1.1 1.1-2.3 1.4-3.6h3a8 8 0 0 1-4.4 3.6zm1.8-5.6a16.5 16.5 0 0 0 0-4h3.4a8 8 0 0 1 0 4z"/></svg>
        www.brindlecrest.ca
      </li>
    </ul>
  </div>
</section>

</body>
</html>
```